brisk-vale.com Real Estate, Investment, Financial corporate

Real Estate, Investment, Financial corporate looking site. Show present a professional firm, with an elegant display. Please see the attached file which includes the logo, palette and fonts.
Updates

We just starting the brief today. ( logo was delayed)

Target Market(s)

Investors, Corporate , B2b

Industry/Entity Type

real-estate investments

Number of Pages Required

3 page

Requirements
Must have
• Dazzling Homepage
Nice to have
• paralex

```html
<!DOCTYPE html>
<html lang="en">
<head>
<meta charset="utf-8">
<title>Brisk-Vale — Homes</title>
<link rel="stylesheet" href="https://fonts.googleapis.com/css2?family=Montserrat:wght@400;500;600;700&family=Playfair+Display:wght@400;700&display=swap">
<style>
:root{
  --orange:#eba45a;
  --orange-dark:#d98c3c;
  --ink:#2b2b2b;
  --muted:#7a7a7a;
  --light:#f3f3f3;
  --black:#121212;
  --white:#fff;
  --sans:'Montserrat',Arial,sans-serif;
  --serif:'Playfair Display',Georgia,serif;
}
*{box-sizing:border-box;margin:0;padding:0}
html,body{width:1200px;height:4640px;overflow:hidden}
body{position:relative;background:var(--white);font-family:var(--sans);color:var(--ink)}
.abs{position:absolute}
.photo{position:absolute}
.btn-outline{position:absolute;border:2px solid var(--orange);border-radius:24px;color:var(--orange);font-size:12px;font-weight:600;letter-spacing:1px;text-align:center;line-height:36px;height:40px;text-transform:uppercase}

/* header */
.site-header{position:absolute;left:0;top:0;width:1200px;height:62px;background:rgba(255,255,255,.96);display:flex;align-items:center;padding:0 150px;z-index:3}
.brand{display:flex;align-items:center;gap:8px;color:var(--orange);font-weight:600;font-size:15px}
.brand-mark{width:14px;height:14px;border:2px solid var(--orange);border-radius:50%}
.main-nav{display:flex;gap:30px;margin-left:70px;font-size:11px;font-weight:600;letter-spacing:.5px}
.main-nav a{color:var(--ink);text-decoration:none}
.main-nav a.active{color:var(--orange)}
.header-phone{margin-left:auto;display:flex;gap:8px;align-items:center;color:var(--orange);font-size:12px;font-weight:600}

/* hero */
.hero-photo{left:0;top:0;width:1200px;height:540px;background:linear-gradient(160deg,#8fb7d8 0%,#c9d6cf 30%,#9aa67a 55%,#d9d2c5 80%,#b8ae9e 100%)}
.hero-card{position:absolute;left:735px;top:112px;width:262px;height:360px;background:var(--orange);color:#fff;padding:26px 22px}
.hero-card .welcome{font-size:22px;text-align:right;font-family:var(--serif)}
.hero-card .name{font-size:22px;text-align:right;font-weight:700;font-family:var(--serif);letter-spacing:1px}
.hero-card .tag{font-size:12px;text-align:right;letter-spacing:1px;margin-top:4px}
.hero-card h3{font-size:16px;font-weight:700;margin-top:30px;letter-spacing:1px}
.field{height:26px;background:#fff;margin-top:10px;font-size:10px;color:#999;padding:7px 8px}
.hero-card .submit{margin-top:14px;height:28px;background:#fff;color:var(--ink);font-size:10px;font-weight:700;text-align:center;line-height:28px;letter-spacing:.5px}
.slider-dots{left:560px;top:532px;display:flex;gap:10px}
.slider-dots span{width:10px;height:10px;border-radius:50%;background:#ccc}
.slider-dots span.on{background:var(--orange)}
.hero-arrows{left:640px;top:460px;display:flex;gap:8px}
.hero-arrows span{width:30px;height:30px;border-radius:50%;background:rgba(255,255,255,.85);font-size:14px;text-align:center;line-height:30px;color:var(--ink)}

/* about */
.about-photo{left:150px;top:620px;width:300px;height:390px;background:linear-gradient(170deg,#9ec1de 0%,#b9c9a3 40%,#e6e2da 70%,#8f9a7a 100%)}
.about-text{left:510px;top:620px;width:540px}
.about-text h2{font-family:var(--serif);font-size:28px;color:var(--orange);font-weight:400}
.about-text h2 span{font-size:20px;color:var(--ink)}
.about-text p{font-size:10.5px;line-height:1.6;color:var(--muted);margin-top:10px}
.amenity-icons{display:grid;grid-template-columns:repeat(4,1fr);gap:22px 10px;margin-top:24px}
.amenity{text-align:center;font-size:9px;color:var(--muted)}
.amenity svg{display:block;margin:0 auto 6px}

/* financial */
.kitchen-photo{left:0;top:1075px;width:1200px;height:525px;background:linear-gradient(120deg,#e9e9ea 0%,#d5d4d2 40%,#f4f4f3 60%,#a9a8a6 100%)}
.features-card{left:160px;top:1250px;width:280px;height:350px;background:var(--orange);color:#fff;padding:30px 28px}
.features-card h2{font-size:34px;font-weight:700;line-height:1}
.features-card h2 span{display:block;font-size:20px;font-weight:500;letter-spacing:1px;margin-top:4px}
.features-card ul{list-style:none;margin-top:18px}
.features-card li{font-size:10px;letter-spacing:.5px;line-height:20px;display:flex;gap:8px;align-items:center}
.features-card li::before{content:"";width:5px;height:5px;border-radius:50%;background:#fff}

/* pet friendly */
.pool-photo{left:0;top:1880px;width:1200px;height:840px;background:linear-gradient(180deg,#5e9fd6 0%,#a7cce6 25%,#6e8f5f 40%,#d8c8ad 55%,#63c6dd 70%,#3aa6c8 100%)}
.pet-wave{left:0;top:1600px;width:1200px;height:450px}
.pet-circle{left:150px;top:1700px;width:300px;height:300px;border-radius:50%;background:radial-gradient(circle at 50% 45%,#f2efe9 0%,#d9cbb6 55%,#b89d7c 100%);border:6px solid #fff;box-shadow:0 0 0 3px var(--orange)}
.pet-text{left:520px;top:1690px;width:520px}
.pet-text .kicker{font-family:var(--serif);font-size:26px;color:var(--orange)}
.pet-text h2{font-family:var(--serif);font-size:44px;color:var(--orange);font-weight:400;line-height:1.1}
.pet-text .sub{font-size:20px;letter-spacing:1px;margin-top:10px;color:var(--ink)}
.pet-text .note{font-size:16px;letter-spacing:1px;color:var(--orange);margin-top:4px}
.pet-rule{left:505px;top:1690px;width:2px;height:240px;background:var(--orange)}

/* community */
.community-banner{left:200px;top:2555px;width:800px;height:82px;background:var(--orange);color:#fff;font-size:34px;font-weight:700;text-align:center;line-height:82px;letter-spacing:1px;box-shadow:0 6px 16px rgba(0,0,0,.12)}
.community-list{left:200px;top:2690px;width:820px;display:grid;grid-template-columns:repeat(3,1fr);gap:10px 30px}
.community-list li{list-style:none;font-size:10.5px;color:var(--orange);letter-spacing:.5px;display:flex;align-items:center;gap:10px;padding-bottom:6px;border-bottom:1px solid #eee}
.community-list li::before{content:"";width:12px;height:12px;background:#ddd;border-radius:2px}

/* testimonials */
.testimonials{left:0;top:2880px;width:1200px;height:540px;background:var(--light)}
.testimonials h2{position:absolute;top:70px;width:1200px;text-align:center;font-size:22px;font-weight:500;letter-spacing:1px}
.testimonials .sub{position:absolute;top:108px;width:1200px;text-align:center;font-size:12px;font-weight:600;letter-spacing:.5px}
.test-card{position:absolute;left:155px;top:185px;width:890px;height:310px;background:#fff;box-shadow:0 4px 18px rgba(0,0,0,.08)}
.test-card .quote{position:absolute;left:40px;top:40px;font-family:var(--serif);font-size:80px;line-height:1;color:var(--ink)}
.test-card .stars{position:absolute;left:60px;top:22px;color:var(--orange);font-size:14px;letter-spacing:3px}
.test-card p{position:absolute;left:40px;top:130px;width:380px;font-size:10.5px;line-height:1.7;color:var(--muted)}
.test-card .who{position:absolute;left:40px;top:255px;font-size:10px;color:var(--ink)}
.test-card .arrows{position:absolute;left:345px;top:45px;font-size:18px;color:var(--ink);letter-spacing:10px}
.test-photo{position:absolute;left:445px;top:-12px;width:440px;height:320px;background:linear-gradient(135deg,#d8d4cf 0%,#eeeae6 45%,#a8a39c 100%)}

/* cta */
.cta-title{left:0;top:3460px;width:1200px;text-align:center;font-family:var(--serif);font-size:34px;line-height:1.3;color:var(--ink)}

/* gallery */
.gallery-main{left:150px;top:3675px;width:450px;height:340px;background:linear-gradient(180deg,#6aa7d8 0%,#8aa77b 40%,#bfb29a 60%,#47b5d2 100%)}
.g{position:absolute;width:210px;height:160px}
.g1{left:610px;top:3675px;background:linear-gradient(135deg,#f2f2f2,#bfbdb9)}
.g2{left:830px;top:3675px;background:linear-gradient(160deg,#7fb3de,#c6b9a1 60%,#8c9a72)}
.g3{left:610px;top:3855px;background:linear-gradient(135deg,#e9e7e4,#9e9a94)}
.g4{left:830px;top:3855px;background:linear-gradient(135deg,#efefef,#a7a7a9)}

/* contact strip */
.contact-strip{left:0;top:4245px;width:1200px;height:95px;background:var(--orange);color:#fff;display:flex;align-items:center;justify-content:center;gap:150px;font-size:13px;font-weight:500}
.contact-item{display:flex;align-items:center;gap:14px}
.contact-item .ring{width:46px;height:46px;border:2px solid #fff;border-radius:50%;display:flex;align-items:center;justify-content:center}

/* footer */
.site-footer{left:0;top:4340px;width:1200px;height:300px;background:var(--black);color:#fff}
.subscribe{position:absolute;left:180px;top:28px;width:840px;height:38px;border:1px solid #555;border-radius:20px;font-size:11px;color:#aaa;padding:11px 20px}
.subscribe span{position:absolute;right:4px;top:3px;height:30px;width:130px;background:#fff;color:var(--ink);border-radius:16px;text-align:center;line-height:30px;font-weight:700;font-size:11px;letter-spacing:1px}
.thanks{position:absolute;top:100px;width:1200px;text-align:center;font-size:26px;font-weight:600}
.foot-nav{position:absolute;top:180px;width:1200px;display:flex;justify-content:center;gap:26px;font-size:11px;font-weight:600;letter-spacing:.5px}
.copyright{position:absolute;left:0;top:260px;width:1200px;text-align:center;font-size:10px;color:#bbb;border-top:1px solid #2a2a2a;padding-top:16px}
</style>
</head>
<body>

<div class="photo hero-photo" role="img" aria-label="Sunlit apartment courtyard with lawn, palm trees and pergola"></div>

<header class="site-header">
  <div class="brand"><span class="brand-mark"></span>Brisk-Vale</div>
  <nav class="main-nav">
    <a class="active">HOME</a><a>GALLERY</a><a>FEATURES/AMENITIES</a><a>FLOOR PLANS</a><a>APPLY ONLINE</a><a>CONTACT US</a>
  </nav>
  <div class="header-phone">
    <svg width="14" height="14" viewBox="0 0 24 24"><path d="M6.6 10.8a15 15 0 0 0 6.6 6.6l2.2-2.2c.3-.3.7-.4 1-.2 1.1.4 2.3.6 3.6.6.6 0 1 .4 1 1V20c0 .6-.4 1-1 1A17 17 0 0 1 3 4c0-.6.4-1 1-1h3.5c.6 0 1 .4 1 1 0 1.3.2 2.5.6 3.6.1.3 0 .7-.2 1z" fill="#eba45a"/></svg>
    +000 41 555 020
  </div>
</header>

<section class="hero-card">
  <div class="welcome">Welcome to</div>
  <div class="name">BRISK-VALE</div>
  <div class="tag">YOUR NEXT BEAUTIFUL HOME</div>
  <h3>REQUEST A CALL</h3>
  <div class="field">Name</div>
  <div class="field">Email</div>
  <div class="field">Phone</div>
  <div class="submit">REQUEST A CALL BACK</div>
</section>
<div class="abs hero-arrows"><span>‹</span><span>›</span></div>
<div class="abs slider-dots"><span class="on"></span><span></span><span></span></div>

<div class="photo about-photo" role="img" aria-label="Two-storey apartment building behind a white fence"></div>
<section class="abs about-text">
  <h2>ABOUT <span>Us</span></h2>
  <p>Our community is conveniently located near the park and main boulevard. Located in a quiet, leafy section close to schools, shopping and dining, our homes offer spacious layouts and bright interiors. Residents enjoy a relaxed setting, helpful on-site staff, easy access to major routes, well kept grounds and a welcoming neighbourhood. Come home to comfort, calm and everyday convenience at a price that fits your plans.</p>
  <div class="amenity-icons">
    <div class="amenity"><svg width="30" height="30" viewBox="0 0 30 30"><circle cx="15" cy="15" r="12" fill="none" stroke="#eba45a" stroke-width="2"/><path d="M15 8v7l5 3" stroke="#eba45a" stroke-width="2" fill="none"/></svg>Minutes from the<br>city freeway</div>
    <div class="amenity"><svg width="30" height="30" viewBox="0 0 30 30"><path d="M4 26V12l11-8 11 8v14z" fill="none" stroke="#eba45a" stroke-width="2"/></svg>Beautiful and quiet<br>community</div>
    <div class="amenity"><svg width="30" height="30" viewBox="0 0 30 30"><rect x="5" y="8" width="20" height="18" fill="none" stroke="#eba45a" stroke-width="2"/><path d="M10 8V4h10v4" stroke="#eba45a" stroke-width="2" fill="none"/></svg>Oversized Modern<br>Apartments</div>
    <div class="amenity"><svg width="30" height="30" viewBox="0 0 30 30"><path d="M4 20c4-8 18-8 22 0" fill="none" stroke="#eba45a" stroke-width="2"/><path d="M4 24h22" stroke="#eba45a" stroke-width="2"/></svg>Sparkling Pool</div>
    <div class="amenity"><svg width="30" height="30" viewBox="0 0 30 30"><rect x="6" y="6" width="18" height="18" rx="2" fill="none" stroke="#eba45a" stroke-width="2"/></svg>Wood Floors</div>
    <div class="amenity"><svg width="30" height="30" viewBox="0 0 30 30"><rect x="5" y="5" width="20" height="20" fill="none" stroke="#eba45a" stroke-width="2"/><circle cx="15" cy="17" r="5" fill="none" stroke="#eba45a" stroke-width="2"/></svg>Washer and Dryer</div>
    <div class="amenity"><svg width="30" height="30" viewBox="0 0 30 30"><path d="M5 25V10h20v15M9 10V5h12v5" fill="none" stroke="#eba45a" stroke-width="2"/></svg>Private Balconies</div>
    <div class="amenity"><svg width="30" height="30" viewBox="0 0 30 30"><circle cx="15" cy="15" r="5" fill="none" stroke="#eba45a" stroke-width="2"/><path d="M15 3v5M15 22v5M3 15h5M22 15h5" stroke="#eba45a" stroke-width="2"/></svg>Secure Community</div>
  </div>
</section>
<div class="btn-outline" style="left:510px;top:968px;width:200px">View more about us</div>

<div class="photo kitchen-photo" role="img" aria-label="Modern kitchen with stainless appliances and dining table"></div>
<section class="abs features-card">
  <h2>FINANCIAL<span>FEATURES</span></h2>
  <ul>
    <li>PET FRIENDLY</li><li>COVERED PARKING</li><li>CENTRAL AIR/HEATING</li><li>STYLE UPGRADE</li><li>GOURMET KITCHEN</li><li>NEW APPLIANCES</li><li>OVERSIZED CLOSETS</li><li>PRIVATE BALCONIES AND PATIOS</li><li>REFRIGERATOR IN ALL UNITS</li><li>WASHER/DRYER IN SELECT UNITS</li>
  </ul>
</section>

<div class="photo pool-photo" role="img" aria-label="Resort-style swimming pool with lounge chairs and palms"></div>
<svg class="abs pet-wave" viewBox="0 0 1200 450" preserveAspectRatio="none" aria-hidden="true">
  <path d="M0 0H1200V300C1000 250 800 380 560 400 330 420 150 330 0 360Z" fill="#fff"/>
  <path d="M0 360C150 330 330 420 560 400 800 380 1000 250 1200 300" fill="none" stroke="#eba45a" stroke-width="3"/>
</svg>
<div class="photo pet-circle" role="img" aria-label="Resident relaxing at home with a pet dog"></div>
<div class="abs pet-rule"></div>
<section class="abs pet-text">
  <div class="kicker">Looking for a</div>
  <h2>Pet friendly<br>Real Estate</h2>
  <div class="sub">COMMUNITY IN FERN BASIN, CA?</div>
  <div class="note">*LOOK NO FURTHER THAN CEDAR ROW VILLAS!</div>
</section>

<div class="abs community-banner">COMMUNITY FEATURES</div>
<ul class="abs community-list">
  <li>CONVENIENT LOCATION</li><li>PLAYGROUND</li><li>PARKING</li>
  <li>ACCESS TO PUBLIC TRANSPORTATION</li><li>CLUBHOUSE</li><li>ON-SITE MAINTENANCE</li>
  <li>LAUNDRY</li><li>COVERED PARKING</li><li>ELECTRONIC PAYMENT</li>
  <li>PARKING</li><li>SPORTS COURT</li><li>BBQ AREAS</li>
  <li>CLOSE TO THE PARK</li><li>GUEST</li><li>POOL</li>
</ul>

<section class="abs testimonials">
  <h2>TENANT TESTIMONIALS</h2>
  <div class="sub">PRAISE FOR CEDAR ROW VILLAS APARTMENT HOMES</div>
  <div class="test-card">
    <div class="quote">“</div>
    <div class="arrows">← →</div>
    <p>Living at the villas has been really lovely. The community is well kept and peaceful, complete with nice grounds, a great pool and kind neighbours. The office team is quick to help and always friendly. We have stayed here three years now and we would gladly recommend it to anyone looking to settle into a new home.</p>
    <div class="who">— Mara Delacroix</div>
    <div class="test-photo" role="img" aria-label="Person working at a laptop with a coffee cup"></div>
  </div>
</section>

<h2 class="abs cta-title">The wait for a beautiful apartment is over, contact<br>us now to schedule an apartment viewing</h2>
<div class="btn-outline" style="left:520px;top:3585px;width:160px">Contact us now</div>

<div class="photo gallery-main" role="img" aria-label="Pool deck with palm trees"></div>
<div class="g g1" role="img" aria-label="Bright open kitchen"></div>
<div class="g g2" role="img" aria-label="Apartment building exterior"></div>
<div class="g g3" role="img" aria-label="Living room interior"></div>
<div class="g g4" role="img" aria-label="Bedroom interior"></div>
<div class="btn-outline" style="left:530px;top:4170px;width:140px;height:32px;line-height:28px;font-size:10px">View gallery</div>

<section class="abs contact-strip">
  <div class="contact-item"><span class="ring"><svg width="20" height="20" viewBox="0 0 24 24"><path d="M6.6 10.8a15 15 0 0 0 6.6 6.6l2.2-2.2c.3-.3.7-.4 1-.2 1.1.4 2.3.6 3.6.6.6 0 1 .4 1 1V20c0 .6-.4 1-1 1A17 17 0 0 1 3 4c0-.6.4-1 1-1h3.5c.6 0 1 .4 1 1 0 1.3.2 2.5.6 3.6.1.3 0 .7-.2 1z" fill="#fff"/></svg></span>+000 41 555 020</div>
  <div class="contact-item"><span class="ring"><svg width="20" height="20" viewBox="0 0 24 24"><rect x="3" y="5" width="18" height="14" fill="none" stroke="#fff" stroke-width="2"/><path d="M3 6l9 7 9-7" fill="none" stroke="#fff" stroke-width="2"/></svg></span>brisk-vale.com</div>
  <div class="contact-item"><span class="ring"><svg width="20" height="20" viewBox="0 0 24 24"><path d="M12 2a7 7 0 0 0-7 7c0 5 7 13 7 13s7-8 7-13a7 7 0 0 0-7-7z" fill="none" stroke="#fff" stroke-width="2"/><circle cx="12" cy="9" r="2.5" fill="#fff"/></svg></span>Linden Court 12,<br>Harrow Bay,<br>Westland</div>
</section>

<footer class="abs site-footer">
  <div class="subscribe">Enter email id<span>SUBSCRIBE</span></div>
  <div class="thanks">Thank you for visiting us</div>
  <nav class="foot-nav"><a>HOME</a><a>|</a><a>GALLERY</a><a>|</a><a>FEATURES</a><a>|</a><a>FLOOR PLANS</a><a>|</a><a>CONTACT US</a></nav>
  <div class="copyright">Copyright © 2020 brisk-vale.com | All Rights Reserved</div>
</footer>

</body>
</html>
```